Corvane Partners Web Design

Dear all
I need a web design for a financial services site. We are a broker who deals with many different financial institutions and require a clean, simple and instantly impressive site based on the colour scheme that SketchGuild created for us. A landing page (www.crvnp.mx) gives an idea of the logo and clour scheme but we are looking at either a one page site with rollover text boxes or a 3 or 4 page site depending on the preference of the designer and the best user experience. The site“s purpose is to give confidence that the company exists rather than impart pages of information although we would like this to be a site that can expand over time as the company grows. For now the requirement is for a clear set of possibly changing images at the centre of a white screen that relate to finance in general nad the benefits of wealth creation as well as sectios either along the top or bottom - Our Company, Our Approach, Our services, Our clients, Contact (user to fill in contact box to be sent to info@crvnp.mx. The text for each of these boxes I assume can be added by the coding team here, it the overall look and feel that I am looking for from SketchGuild - deadline can be extended if necessary but I was hoping to wrap this all up in October

Target Market(s)

Succesful individuals looking to maximise returns on their investment via world class financial institutions and supported throughout by qualified independent financial advisors

Industry/Entity Type

Finance

Requirements
Must have
• Logo and color scheme of the logo design SketchGuild sent - I have all these sourcefiles, pantone and fonts

```html
<!DOCTYPE html>
<html lang="en">
<head>
<meta charset="utf-8">
<title>Corvane Partners</title>
<link rel="stylesheet" href="https://fonts.googleapis.com/css2?family=Michroma&family=Questrial&display=swap">
<style>
:root{
  --navy:#172c57;
  --orange:#eda23a;
  --grey:#6d6f73;
  --white:#ffffff;
  --black:#000000;
  --ink:#1a1a1a;
  --mail-blue:#1f6db3;
  --video-red:#b0161b;
}
*{margin:0;padding:0;box-sizing:border-box}
html,body{width:982px;height:1200px;overflow:hidden;background:var(--white)}
.page{position:relative;width:982px;height:1200px;font-family:"Questrial",sans-serif;color:var(--ink)}
.abs{position:absolute}

/* header */
.brand{left:108px;top:58px;display:flex;align-items:center;gap:8px}
.brand-dot{width:14px;height:14px;border-radius:50%;background:var(--navy)}
.brand-name{font-family:"Questrial",sans-serif;font-size:17px;letter-spacing:5px;color:var(--navy);line-height:1.1}
.account{right:111px;top:28px;font-size:12px;letter-spacing:1px;color:var(--orange)}
.account span{margin:0 6px}
.main-nav{left:333px;top:88px;display:flex;font-size:12px;letter-spacing:.6px}
.main-nav a{color:var(--ink);text-decoration:none;height:23px;line-height:25px;margin-right:21px}
.main-nav a.is-active{background:var(--orange);color:var(--white);padding:0 4px;margin-right:18px}
.main-nav a:last-child{margin-right:0}

/* hero */
.hero{left:0;top:111px;width:982px;height:230px;background:linear-gradient(120deg,#c9d9ea 0%,#7fa3cc 35%,#b7cde4 60%,#5e88b9 100%)}
.slider-dots{left:158px;top:301px;display:flex;align-items:center;gap:5px}
.slider-dots i{display:block;width:18px;height:18px;border-radius:50%;background:var(--navy)}
.slider-dots i.is-current{width:24px;height:24px;background:var(--orange)}

/* section titles */
.section-title{font-size:20px;letter-spacing:1px;color:var(--orange);font-weight:400}
.why-title{left:0;width:982px;top:346px;text-align:center}

/* feature cards */
.feature{top:380px;width:216px;height:286px;background:var(--navy);text-align:center}
.feature::before{content:"";display:block;height:14px;background:var(--grey)}
.feature svg{display:block;margin:8px auto 0;height:64px}
.feature h3{font-family:"Michroma",sans-serif;font-weight:400;font-size:11px;color:var(--orange);margin-top:12px;letter-spacing:.3px}
.feature p{font-family:"Michroma",sans-serif;font-size:7.4px;line-height:20.7px;color:var(--white);text-align:left;padding:12px 14px 0 17px}

/* how it works */
.how{left:0;top:690px;width:982px;height:201px;background:var(--navy)}
.how-title{left:134px;top:698px}
.how-text{left:125px;top:734px;width:470px;font-family:"Michroma",sans-serif;font-size:7.4px;line-height:20.7px;color:var(--white)}
.video{left:669px;top:718px;width:188px;height:147px;background:var(--black)}
.video-frame{position:absolute;left:0;top:0;width:188px;height:139px;background:radial-gradient(circle at 45% 45%,#f3c25a 0%,#c9801f 45%,#6b2f08 100%)}
.video-play{position:absolute;left:68px;top:44px}
.video-bar{position:absolute;left:0;bottom:0;width:188px;height:8px;background:#1b1b1b}

/* call block */
.call{left:199px;top:914px;width:598px;height:130px;background:var(--navy);border-radius:2px;overflow:hidden}
.call-wave{position:absolute;left:0;top:0}
.phone-icon{left:238px;top:928px}
.call-btn{left:276px;top:948px;width:172px;height:31px;background:var(--orange);color:var(--white);font-size:15px;letter-spacing:1px;text-align:center;line-height:32px}
.call-phone{left:497px;top:924px;font-family:"Michroma",sans-serif;font-size:19px;color:var(--white)}
.mail-icon{left:466px;top:958px}
.call-mail{left:513px;top:963px;font-family:"Michroma",sans-serif;font-size:15px;color:var(--white)}
.guarantee{left:199px;width:598px;top:1017px;text-align:center;font-family:"Michroma",sans-serif;font-size:14px;color:var(--white)}

/* footer */
.footer{left:0;top:1071px;width:982px;height:129px;background:var(--black);color:var(--white)}
.subscribe-title{left:108px;top:1110px;font-family:"Michroma",sans-serif;font-size:11.5px;letter-spacing:.5px;color:var(--white)}
.subscribe-text{left:110px;top:1134px;font-size:10.5px;line-height:13px;color:var(--white)}
.subscribe-input{left:108px;top:1161px;width:118px;height:13px;border-radius:7px;background:#e6e6e6;font-size:5.5px;color:#8a8a8a;text-align:center;line-height:13px}
.subscribe-go{left:230px;top:1159px;width:18px;height:18px;border-radius:50%;background:var(--orange);font-size:7px;line-height:18px;text-align:center;color:var(--white)}
.footer-nav{left:287px;top:1147px;display:flex;gap:14px;font-size:8.5px;letter-spacing:.3px;color:var(--white)}
.copyright{left:0;width:982px;top:1169px;text-align:center;font-size:8px;letter-spacing:.3px;color:var(--white)}
.footer-brand{left:705px;top:1152px;display:flex;align-items:center;gap:8px}
.footer-brand .brand-dot{background:var(--white)}
.footer-brand .brand-name{color:var(--white);font-size:15px;letter-spacing:4px}
</style>
</head>
<body>
<div class="page">

  <header>
    <div class="abs brand"><span class="brand-dot"></span><span class="brand-name">CORVANE PARTNERS</span></div>
    <div class="abs account">LOGIN<span>I</span>REGISTER</div>
    <nav class="abs main-nav">
      <a class="is-active" href="#">HOME</a>
      <a href="#">OUR COMPANY</a>
      <a href="#">OUR APPROACH</a>
      <a href="#">OUR SERVICES</a>
      <a href="#">OUR CLIENTS</a>
      <a href="#">CONTACT</a>
    </nav>
  </header>

  <div class="abs hero" role="img" aria-label="Blue-toned photo of coins, a financial spreadsheet, a fountain pen and a calculator"></div>
  <div class="abs slider-dots"><i class="is-current"></i><i></i><i></i><i></i><i></i></div>

  <h2 class="abs section-title why-title">WHY CHOOSE US?</h2>

  <article class="abs feature" style="left:108px">
    <svg viewBox="0 0 100 64" width="100" fill="none" stroke="#fff" stroke-width="3">
      <rect x="4" y="20" width="48" height="30"/><path d="M22 50v7M14 58h28"/>
      <rect x="42" y="4" width="52" height="32" fill="#172c57"/><path d="M62 36v8M54 45h20"/>
      <path d="M38 24v-8a10 10 0 0 1 20 0"/>
    </svg>
    <h3>EASY TO UNDERSTAND</h3>
    <p>Lorem Ipsum is simply dummy text of the printing and typesetting industry. Lorem Ipsum has been the industry's standard dummy text ever since the 1500s, when an unknown printer took a galley of type and scrambled it to make a type specimen book. It has</p>
  </article>

  <article class="abs feature" style="left:383px">
    <svg viewBox="0 0 64 64" width="64" fill="none" stroke="#fff" stroke-width="3">
      <circle cx="32" cy="32" r="29"/><circle cx="32" cy="32" r="23"/>
      <path d="M32 16v17h12" stroke-linecap="round"/>
    </svg>
    <h3>SAVE TIME &amp; MONEY</h3>
    <p>Lorem Ipsum is simply dummy text of the printing and typesetting industry. Lorem Ipsum has been the industry's standard dummy text ever since the 1500s, when an unknown printer took a galley of type and scrambled it to make a type specimen book. It has</p>
  </article>

  <article class="abs feature" style="left:656px">
    <svg viewBox="0 0 64 64" width="64">
      <path fill="#fff" d="M32 2l6 6 8-2 3 8 8 3-2 8 6 7-6 7 2 8-8 3-3 8-8-2-6 6-6-6-8 2-3-8-8-3 2-8-6-7 6-7-2-8 8-3 3-8 8 2z"/>
      <circle cx="32" cy="33" r="16" fill="#172c57"/>
      <path d="M24 33l6 6 11-12" fill="none" stroke="#fff" stroke-width="4" stroke-linecap="round" stroke-linejoin="round"/>
    </svg>
    <h3>HIGH QUALITY REPORTS</h3>
    <p>Lorem Ipsum is simply dummy text of the printing and typesetting industry. Lorem Ipsum has been the industry's standard dummy text ever since the 1500s, when an unknown printer took a galley of type and scrambled it to make a type specimen book. It has</p>
  </article>

  <section class="abs how"></section>
  <h2 class="abs section-title how-title">HOW IT WORKS</h2>
  <p class="abs how-text">Lorem Ipsum is simply dummy text of the printing and typesetting industry. Lorem Ipsum has been the industry's standard dummy text ever since the 1500s, when an unknown printer took a galley of type and scrambled it to make a type specimen book. It has survived not only five centuries, but also the leap into electronic typesetting, remaining essentially unchanged. It was popularised in the 1960s with the release of Lettrafix sheets containing Lorem Ipsum passages, and more recently with desktop publishing software like Pagewright Studio including versions of Lorem Ipsum.</p>
  <div class="abs video">
    <div class="video-frame" role="img" aria-label="Video still of stacked banknotes, coins and a pocket watch in warm golden light"></div>
    <svg class="video-play" width="58" height="58" viewBox="0 0 58 58"><circle cx="29" cy="29" r="29" fill="var(--video-red)"/><path d="M22 16l20 13-20 13z" fill="#fff"/></svg>
    <div class="video-bar"></div>
  </div>

  <section class="abs call">
    <svg class="call-wave" width="598" height="130" viewBox="0 0 598 130">
      <path d="M0 92 Q300 86 598 92 L598 130 L0 130 Z" fill="var(--orange)"/>
    </svg>
  </section>
  <svg class="abs phone-icon" width="31" height="31" viewBox="0 0 31 31">
    <rect width="31" height="31" rx="4" fill="#fff"/>
    <path d="M11 6h4v6h-3c0 3 1 6 3 8h3v5h-4c-5-3-7-11-3-19z" fill="var(--navy)"/>
  </svg>
  <div class="abs call-btn">CALL US TODAY</div>
  <div class="abs call-phone">555-010-777</div>
  <svg class="abs mail-icon" width="32" height="32" viewBox="0 0 32 32">
    <circle cx="16" cy="16" r="16" fill="var(--mail-blue)"/>
    <rect x="8" y="10" width="16" height="12" rx="2" fill="#fff"/>
    <path d="M8 11l8 6 8-6" fill="none" stroke="var(--mail-blue)" stroke-width="1.5"/>
  </svg>
  <div class="abs call-mail">info@crvnp.mx</div>
  <div class="abs guarantee">100% satisfaction gurantee.</div>

  <footer class="abs footer"></footer>
  <div class="abs subscribe-title">SUBSCRIBE TODAY!</div>
  <div class="abs subscribe-text">Sign up to our program<br>and promote ..</div>
  <div class="abs subscribe-input">YOUR EMAIL HERE</div>
  <div class="abs subscribe-go">GO</div>
  <nav class="abs footer-nav">
    <span>HOME</span><span>OUR COMPANY</span><span>OUR APPROACH</span><span>OUR SERVICES</span><span>OUR CLIENTS</span><span>CONTACT</span>
  </nav>
  <div class="abs copyright">COPY-RIGHT ALL RESERVED</div>
  <div class="abs footer-brand"><span class="brand-dot"></span><span class="brand-name">CORVANE PARTNERS</span></div>

</div>
</body>
</html>
```